Howard Lindqvist and Dennis Ashworth Advertisement

We would like an ad that conveys understated elegance. We are a company that purchases estate jewelry watches and diamonds. We care to a wealthy, upscale clientele.

Target Market(s)

Wealthy upscale.

Industry/Entity Type

It Company

Requirements
Must have
• Elegant Design. Crisp Clean. Attached a doc of how the ad should be arranged.

```html
<!DOCTYPE html>
<html lang="en">
<head>
<meta charset="utf-8">
<title>Howard Lindqvist &amp; Dennis Ashworth — Ready to Sell?</title>
<link rel="stylesheet" href="https://fonts.googleapis.com/css2?family=Cinzel:wght@400;700&amp;family=Cormorant+SC:wght@500;600&amp;display=swap">
<style>
  :root {
    --frame: #c9c9cb;
    --panel: #ececed;
    --panel-light: #f7f7f8;
    --ink: #2a2a2c;
    --ink-soft: #4a4a4d;
    --rule: #8f8f93;
    --gem-light: #ffffff;
    --gem-mid: #d9dadd;
    --gem-dark: #9c9ea3;
  }
  * { margin: 0; padding: 0; box-sizing: border-box; }
  html, body { width: 849px; height: 1200px; overflow: hidden; background: var(--frame); }
  .ad {
    position: relative;
    width: 849px;
    height: 1200px;
    background: linear-gradient(90deg, #bdbdbf 0%, var(--frame) 6%, var(--frame) 94%, #bdbdbf 100%);
    font-family: "Cinzel", serif;
    color: var(--ink);
  }
  .ad__panel {
    position: absolute;
    left: 52px; right: 52px; top: 30px; bottom: 20px;
    background: radial-gradient(ellipse at 50% 35%, var(--panel-light) 0%, var(--panel) 60%, #e4e4e6 100%);
  }
  .ad__headline {
    position: absolute; top: 188px; left: 0; right: 0;
    text-align: center; font-weight: 700; font-size: 28px; letter-spacing: 3px;
  }
  .ad__gem {
    position: absolute; left: 268px; top: 298px; width: 330px; height: 292px;
    background:
      radial-gradient(circle at 22% 22%, rgba(255,255,255,1) 0%, rgba(255,255,255,0) 30%),
      linear-gradient(135deg, var(--gem-light) 0%, var(--gem-mid) 45%, var(--gem-dark) 100%);
    transform: rotate(8deg);
    clip-path: polygon(8% 0, 92% 0, 100% 9%, 100% 91%, 92% 100%, 8% 100%, 0 91%, 0 9%);
  }
  .ad__promise {
    position: absolute; top: 684px; left: 0; right: 0;
    text-align: center; font-size: 24px; letter-spacing: 9px; color: var(--ink-soft);
  }
  .ad__promise-rule {
    position: absolute; top: 724px; left: 296px; width: 232px; height: 1px; background: var(--rule);
  }
  .ad__appointment {
    position: absolute; top: 738px; left: 0; right: 0;
    text-align: center; font-size: 15px; letter-spacing: 3px; color: var(--ink-soft);
  }
  .brand { position: absolute; top: 912px; left: 0; right: 0; text-align: center; }
  .brand__name {
    font-family: "Cormorant SC", serif; font-weight: 500; font-size: 22px; letter-spacing: 1px; color: var(--ink-soft);
  }
  .brand__tagline {
    display: flex; align-items: center; justify-content: center; gap: 8px;
    margin-top: 2px; font-family: "Cormorant SC", serif; font-size: 11px; letter-spacing: 1px; color: var(--ink-soft);
  }
  .brand__tagline::before, .brand__tagline::after {
    content: ""; width: 86px; height: 1px; background: var(--rule);
  }
  .contact { position: absolute; top: 1040px; left: 0; right: 0; text-align: center; color: var(--ink); }
  .contact__venue { font-family: "Cormorant SC", serif; font-weight: 600; font-size: 15px; letter-spacing: 1px; }
  .contact__address { font-family: "Cormorant SC", serif; font-size: 13px; margin-top: 6px; color: var(--ink-soft); }
  .contact__rule { width: 430px; height: 1px; margin: 8px auto 6px; background: var(--rule); }
  .contact__lines {
    font-family: "Cormorant SC", serif; font-weight: 600; font-size: 17px; letter-spacing: 1px;
    display: flex; justify-content: center; gap: 22px;
  }
</style>
</head>
<body>
<main class="ad">
  <div class="ad__panel"></div>
  <h1 class="ad__headline">READY TO SELL?</h1>
  <div class="ad__gem" role="img" aria-label="Photograph of a large emerald-cut diamond catching the light"></div>
  <p class="ad__promise">UTMOST DISCRETION</p>
  <div class="ad__promise-rule"></div>
  <p class="ad__appointment">BY APPOINTMENT</p>
  <div class="brand">
    <p class="brand__name">Howard Lindqvist &amp; Dennis Ashworth</p>
    <p class="brand__tagline">your best option</p>
  </div>
  <address class="contact" style="font-style:normal">
    <p class="contact__venue">VIA SERENATA</p>
    <p class="contact__address">118-b alder court, harbor point, fl 33999</p>
    <div class="contact__rule"></div>
    <p class="contact__lines"><span>hello@lindqvistashworth.com</span><span>|</span><span>555.014.2290</span></p>
  </address>
</main>
</body>
</html>
```